Corporate Web Redesign Project - coded

We would like redesign/refresh of our current site that would allow us to increase the depth of content and create a high quality impression for visitors.

Current site - http://corvanisystems.example/

A previous web redesign project has improved our site but it has not really reached the level we require.

Our customers are global, blue chip, organisations and a professional, corporate style of site is required.

Please note we would prefer a coded website to a just a design. We are happy to provide a zip of our current site if required.
Updates

                                   

Target Market(s)

Global oil and gas producers, KT, Pardo, Valmira etc.

Industry/Entity Type

It Professional

Requirements
Must have
• Design should support the level of content we currently have in the existing sitemap - although it should be expandable a site design for a large / complex site would not be appropriate

All current content / pages to be reflected in design

Must be visually appealing

Intuitive and clear navigation that is expandable

Display a high level of professionalism

Use a consistent palette of colours that complements our logo

Clean and organized layout

A way to capture visitor’s information or Call to action (i.e. contact link or form) on every page

Prominent Contact Information
Should not have
• Flash

```html
<!DOCTYPE html>
<html lang="en">
<head>
<meta charset="utf-8">
<title>Corvani Systems</title>
<link href="https://fonts.googleapis.com/css2?family=Open+Sans:ital,wght@0,400;0,600;0,700;1,400&display=swap" rel="stylesheet">
<style>
:root{
  --dark:#3d4046;
  --dark-2:#45484e;
  --teal:#2fb0bd;
  --teal-dark:#27a0ac;
  --text:#333538;
  --muted:#777a7e;
  --line:#e4e4e4;
  --soft:#f8f8f8;
  --white:#ffffff;
}
*{margin:0;padding:0;box-sizing:border-box}
html,body{width:1200px;height:1000px;overflow:hidden}
body{font-family:"Open Sans",Arial,sans-serif;color:var(--text);background:var(--white)}
.wrap{width:1010px;margin:0 auto;position:relative}

.top-bar{height:42px;background:var(--dark)}
.top-bar .wrap{display:flex;justify-content:space-between;align-items:center;height:42px}
.top-bar__name{color:#a9acb0;font-size:12.5px;letter-spacing:.2px}
.top-bar__call{color:#a9acb0;font-size:12.5px;display:flex;align-items:center;gap:8px}
.top-bar__call strong{color:#fff;font-weight:600}

.site-header{height:80px;background:var(--white);border-bottom:1px solid var(--line)}
.site-header .wrap{display:flex;align-items:center;height:80px}
.brand{display:flex;align-items:center;gap:9px;width:225px}
.brand__dot{width:26px;height:26px;border-radius:50%;background:var(--teal)}
.brand__name{font-size:15px;font-weight:700;color:var(--dark);letter-spacing:.5px}
.main-nav{display:flex;gap:33px;height:80px}
.main-nav a{font-size:14.5px;color:var(--text);text-decoration:none;display:flex;align-items:center;gap:8px;height:80px}
.main-nav a.is-active{color:var(--teal);border-bottom:2px solid var(--teal)}
.search{margin-left:auto;width:95px;height:33px;border:1px solid #dcdcdc;border-radius:2px;display:flex;align-items:center;gap:8px;padding-left:11px;font-size:12.5px;font-style:italic;color:#a3a3a3}

.hero{height:440px;background:radial-gradient(ellipse at 55% 45%,#f4f4f4 0%,#e4e4e4 60%,#d6d6d6 100%);position:relative;overflow:hidden}
.hero__visual{position:absolute;left:410px;top:20px;width:710px;height:420px;background:linear-gradient(90deg,rgba(225,225,225,0) 0%,#d9dcdd 35%,#e9e6e2 70%,#d4cfc8 100%)}
.hero__copy{position:absolute;left:96px;top:128px}
.hero__title{font-size:42px;font-weight:600;color:var(--text);line-height:1.1}
.hero__sub{font-size:23px;color:var(--text);margin-top:12px}
.btn-light{display:inline-block;margin-top:24px;background:#fff;border:1px solid #e2e2e2;padding:8px 22px;font-size:13px;color:var(--text);box-shadow:0 1px 2px rgba(0,0,0,.08)}
.hero__dots{position:absolute;left:572px;top:404px;display:flex;gap:7px}
.hero__dots span{width:14px;height:14px;border-radius:50%;background:#8a8a8a}
.hero__dots span.is-on{background:var(--teal)}

.tagline{height:81px;background:var(--dark-2);display:flex;align-items:center;justify-content:center;font-size:18px;color:#e8e8e8;gap:6px}
.tagline a{color:var(--teal);font-style:italic;text-decoration:none;display:flex;align-items:center;gap:6px}

.solutions{height:213px;background:var(--soft);border-bottom:1px solid var(--line)}
.solutions .wrap{display:flex;padding-top:40px}
.solution{width:344px;display:flex;gap:16px}
.solution__icon{width:62px;height:62px;border-radius:50%;background:#fff;border:1px solid #e1e1e1;display:flex;align-items:center;justify-content:center;flex-shrink:0}
.solution h3{font-size:16px;font-weight:600;color:var(--text);margin-top:-2px}
.solution p{font-size:12.8px;color:var(--muted);line-height:20px;margin-top:8px;width:245px}
.btn-teal{display:inline-block;margin-top:17px;background:var(--teal);border:1px solid var(--teal-dark);color:#fff;font-size:13px;font-weight:600;padding:8px 23px;border-radius:2px}

.projects .wrap{padding-top:43px}
.projects__head{display:flex;align-items:center;gap:18px}
.projects__head h2{font-size:18px;font-weight:600;color:var(--text)}
.projects__rule{flex:1;height:12px;background:repeating-linear-gradient(135deg,#e3e3e3 0 2px,transparent 2px 5px)}
.projects__grid{display:flex;gap:24px;margin-top:26px}
.project{width:320px;height:80px}
.project--rig{background:linear-gradient(180deg,#a9a7b0,#c9b7b3)}
.project--sunset{background:linear-gradient(180deg,#c93a10,#f07a28)}
.project--dusk{background:linear-gradient(180deg,#c4524a,#e98560)}
</style>
</head>
<body>
<header>
  <div class="top-bar">
    <div class="wrap">
      <span class="top-bar__name">CORVANI SYSTEMS</span>
      <span class="top-bar__call">
        <svg width="13" height="13" viewBox="0 0 24 24" fill="#8d9095"><path d="M6.6 10.8a15 15 0 0 0 6.6 6.6l2.2-2.2c.3-.3.7-.4 1-.2 1.1.4 2.3.6 3.6.6.6 0 1 .4 1 1V20c0 .6-.4 1-1 1A17 17 0 0 1 3 4c0-.6.4-1 1-1h3.5c.6 0 1 .4 1 1 0 1.3.2 2.5.6 3.6.1.3 0 .7-.2 1z"/></svg>
        Call us: <strong>+44(0)1632 960418 or (555) 014 2290</strong>
      </span>
    </div>
  </div>
  <div class="site-header">
    <div class="wrap">
      <div class="brand"><span class="brand__dot"></span><span class="brand__name">CORVANI SYSTEMS</span></div>
      <nav class="main-nav">
        <a class="is-active" href="#">Home</a>
        <a href="#">News</a>
        <a href="#">About Us</a>
        <a href="#">Solutions</a>
        <a href="#"><svg width="14" height="11" viewBox="0 0 14 11"><rect width="14" height="11" rx="1" fill="#c3c5c8"/><path d="M0 1l7 5 7-5" stroke="#fff" stroke-width="1.3" fill="none"/></svg>Contact Us</a>
      </nav>
      <div class="search">
        <svg width="12" height="12" viewBox="0 0 12 12"><circle cx="5" cy="5" r="3.8" stroke="#9a9a9a" stroke-width="1.6" fill="none"/><path d="M8 8l3 3" stroke="#9a9a9a" stroke-width="1.8"/></svg>
        Search..
      </div>
    </div>
  </div>
</header>

<main>
  <section class="hero">
    <div class="hero__visual" role="img" aria-label="Photo of a businesswoman drawing a rising bar chart with a teal growth arrow"></div>
    <div class="hero__copy">
      <h1 class="hero__title">Learn &amp; Improve</h1>
      <p class="hero__sub">Performance</p>
      <span class="btn-light">Read More</span>
    </div>
    <div class="hero__dots"><span class="is-on"></span><span></span><span></span></div>
  </section>

  <section class="tagline">
    Our solutions are used in more than 30 countries to support operations...
    <a href="#">More <svg width="16" height="16" viewBox="0 0 16 16"><circle cx="8" cy="8" r="8" fill="#2fb0bd"/><path d="M6.5 4.5L10 8l-3.5 3.5" stroke="#fff" stroke-width="2" fill="none"/></svg></a>
  </section>

  <section class="solutions">
    <div class="wrap">
      <article class="solution">
        <div class="solution__icon">
          <svg width="16" height="24" viewBox="0 0 16 24"><path d="M1 1h14M1 23h14" stroke="#222" stroke-width="2"/><path d="M2.5 2h11c0 5-5 7-5 10s5 5 5 10h-11c0-5 5-7 5-10s-5-5-5-10z" fill="none" stroke="#222" stroke-width="1.4"/><path d="M4 21c1-3 3-4 4-4s3 1 4 4z" fill="#222"/></svg>
        </div>
        <div>
          <h3>Time &amp; Cost Estimation</h3>
          <p>QRX delivers a standardized, systematic approach to understanding project risk.Using QRX Templates you can..</p>
          <span class="btn-teal">Know More</span>
        </div>
      </article>
      <article class="solution">
        <div class="solution__icon">
          <svg width="24" height="26" viewBox="0 0 24 26"><rect x="1" y="1" width="22" height="24" rx="3" fill="#222"/><rect x="4" y="4" width="16" height="5" fill="#fff"/><g fill="#fff"><rect x="4" y="11" width="3" height="3"/><rect x="8.5" y="11" width="3" height="3"/><rect x="13" y="11" width="3" height="3"/><rect x="17" y="11" width="3" height="3"/><rect x="4" y="15.5" width="3" height="3"/><rect x="8.5" y="15.5" width="3" height="3"/><rect x="13" y="15.5" width="3" height="3"/><rect x="17" y="15.5" width="3" height="3"/><rect x="4" y="20" width="3" height="3"/><rect x="8.5" y="20" width="3" height="3"/><rect x="13" y="20" width="3" height="3"/><rect x="17" y="20" width="3" height="3"/></g></svg>
        </div>
        <div>
          <h3>Materials &amp; Cost Control</h3>
          <p>MCX has been helping companies optimize materials and cost tracking processes since 1992.</p>
          <span class="btn-teal">Know More</span>
        </div>
      </article>
      <article class="solution">
        <div class="solution__icon">
          <svg width="26" height="26" viewBox="0 0 26 26"><rect x="1.5" y="1.5" width="23" height="23" rx="5" fill="none" stroke="#222" stroke-width="2.2"/><g fill="#222"><rect x="6" y="7" width="2" height="2"/><rect x="10" y="7" width="10" height="2"/><rect x="6" y="12" width="2" height="2"/><rect x="10" y="12" width="10" height="2"/><rect x="6" y="17" width="2" height="2"/><rect x="10" y="17" width="10" height="2"/></g></svg>
        </div>
        <div>
          <h3>Lessons Learned</h3>
          <p>LKX is an advanced lessons learned &amp; knowledge system for use in the energy industry.</p>
          <span class="btn-teal">Know More</span>
        </div>
      </article>
    </div>
  </section>

  <section class="projects">
    <div class="wrap">
      <div class="projects__head"><h2>Recent Projects</h2><span class="projects__rule"></span></div>
      <div class="projects__grid">
        <div class="project project--rig" role="img" aria-label="Photo of offshore drilling rig towers and cranes"></div>
        <div class="project project--sunset" role="img" aria-label="Photo of an orange sunset sky over the sea"></div>
        <div class="project project--dusk" role="img" aria-label="Photo of an oil rig silhouette at dusk"></div>
      </div>
    </div>
  </section>
</main>
</body>
</html>
```